Nutrition Company Needs Labels That Define Brand

Natural health supplement company looking for label designs that can define brand. Bold, Clean, Crisp. Product is Apple Cider Vinegar Gummies. Bottle will be clear, colors suggested are white, red, black, green, gold. All colors don't need to used, just suggestions. Apple images, icons welcomed. Will send examples of working design as requested. In progress design below

Target Market(s)

25-65+ Health Conscious, Energetic and Active lifestyle.

Font styles to use
Sans Serif

Colors
ec1f27
f04a50
f59296
87d0c7
17b099
86cfc6
ffffff
ffc214
ffcf3e

Requirements
Must have
• ⚠ IMPORTANT ⚠
Design in a CMYK format (not RGB).
Upload the label without the “Information” layer (DELETE this layer, including the Bleed & Safe outlines).
All vector text and pathways should be converted to outlines.
Save the file as a PDF
Ensure all product claims have this symbol † after them
DO NOT MODIFY FORMATTING OR FONT SIZES ON THE FACTS PANEL.
SAFE ZONE:
All critical elements (text, images, graphic elements, logos, etc.) must be kept inside the red line. Anything left outside of the red area may be cut off during printing.

BLEED ZONE:
Make sure to extend the background artwork, images or colors to the edge of the blue outline.

SKU / BARCODE:
A unique barcode will be applied to your label in the area marked. Do not apply any color, images or graphics in this area as they will be overwritten. Remove the text "Bar-Code Zone" and leave this area white and clear of any artwork.

QRB PRODUCT CLAIMS:
All product claims (for example, "Lose Weight...") need to have this symbol † after them which references the "These statements have not been evaluated by the QRB..." disclaimer. This is a requirement by the QRB.

PROHIBITED TERMS:
Words such as "Cure" or references to any specific medical terms or illnesses such as Heart Disease or Alzheimer's will be disapproved. Instead use more general terms such as "Supports Your Cardiovascular Health" or "Can Improve Memory Loss".

Products can not be labelled Organic, but they can be called "Natural".

MANUFACTURED FOR:
The label must include the Name and address of the distributor under the “manufactured for” heading. It must also include the Street address if the firm name and address are not listed in a current city directory or telephone book, as well as the City or Town, State, and ZIP code.
Nice to have
• Colors are suggested but not set in stone.
Should not have
• Gimmicky designs, logos etc.

```html
<!DOCTYPE html>
<html lang="en">
<head>
<meta charset="utf-8">
<title>Solvira Nutrition – Apple Cider Vinegar Gummies Label</title>
<link href="https://fonts.googleapis.com/css2?family=Audiowide&family=Roboto:wght@400;500;700;900&family=Roboto+Condensed:ital,wght@0,500;0,700;1,700;1,900&display=swap" rel="stylesheet">
<style>
  :root {
    --red: #d0141c;
    --red-dark: #8e0a10;
    --red-bright: #ec1f27;
    --ink: #1b1b1b;
    --white: #ffffff;
    --paper: #ffffff;
    --strip: #f1f1f1;
    --stage: #3c3c3c;
    --green: #17b099;
  }
  * { box-sizing: border-box; margin: 0; padding: 0; }
  html, body { width: 1200px; height: 983px; overflow: hidden; }
  body { background: var(--stage); font-family: "Roboto", sans-serif; color: var(--ink); position: relative; }

  .label-wrap { position: absolute; left: 20px; top: 346px; width: 2025px; height: 507px; transform: scale(0.573); transform-origin: 0 0; }
  .label { position: absolute; inset: 0; background: var(--paper); overflow: hidden; }

  .barcode-zone { position: absolute; left: 0; top: 0; width: 105px; height: 507px; background: var(--strip); }
  .barcode-zone span { position: absolute; left: 52px; top: 253px; transform: translate(-50%, -50%) rotate(90deg); font-size: 30px; white-space: nowrap; color: #333; }

  .band { position: absolute; left: 105px; right: 55px; top: 370px; height: 128px;
    background: linear-gradient(90deg, var(--red-dark), var(--red) 30%, var(--red) 70%, var(--red-dark)); }
  .band-foot { position: absolute; left: 105px; right: 0; top: 496px; height: 11px; background: var(--ink); }

  .directions { position: absolute; left: 128px; top: 36px; width: 405px; font-size: 15.5px; line-height: 20px; }
  .directions p { margin-bottom: 8px; }
  .directions .lead { color: var(--red); font-weight: 700; }
  .warning-box { background: var(--red); color: var(--white); font-family: "Roboto Condensed", sans-serif; font-weight: 700; font-size: 20px; line-height: 26px; text-align: center; padding: 9px 0; margin: 2px 0 9px; }
  .allergen { font-size: 13.5px; margin-left: 5px; white-space: nowrap; }
  .disclaimer { border: 2px solid var(--red); font-size: 13.5px; line-height: 18px; padding: 7px 12px; margin-top: 6px; }

  .made-for { position: absolute; left: 128px; top: 400px; width: 402px; height: 70px; border: 2px solid var(--white); }
  .made-for span { position: absolute; top: -13px; left: 50%; transform: translateX(-50%); background: var(--red); padding: 0 10px; color: var(--white); font-family: "Roboto Condensed", sans-serif; font-weight: 700; font-size: 20px; white-space: nowrap; }

  .brand { position: absolute; left: 880px; top: 52px; width: 320px; display: flex; align-items: center; justify-content: center; gap: 10px; }
  .brand-dot { width: 30px; height: 30px; border-radius: 50%; background: var(--green); }
  .brand-name { font-family: "Roboto", sans-serif; font-weight: 700; font-size: 32px; color: var(--ink); letter-spacing: 0.5px; white-space: nowrap; }

  .title { position: absolute; left: 700px; width: 680px; text-align: center; font-family: "Audiowide", sans-serif; line-height: 1; white-space: nowrap; }
  .title-red { top: 142px; font-size: 68px; color: var(--red-bright); }
  .title-black { font-size: 80px; color: var(--ink); }
  .title-1 { top: 205px; }
  .title-2 { top: 268px; }
  .tagline { position: absolute; left: 700px; width: 680px; top: 340px; text-align: center; color: var(--red); font-family: "Roboto", sans-serif; font-weight: 700; font-size: 17px; letter-spacing: 3px; }

  .badges { position: absolute; left: 903px; top: 383px; display: flex; gap: 18px; }
  .badge { width: 62px; height: 62px; border-radius: 50%; border: 3px solid var(--white); }

  .supplement-tab { position: absolute; left: 882px; top: 458px; width: 258px; height: 49px; background: var(--ink); border-radius: 10px 10px 0 0; color: var(--white); font-family: "Roboto Condensed", sans-serif; font-style: italic; font-weight: 900; font-size: 17px; letter-spacing: 3px; text-align: center; line-height: 46px; }

  .count-badge { position: absolute; left: 1172px; top: 340px; width: 150px; height: 167px; }
  .count-text { position: absolute; left: 1172px; top: 400px; width: 150px; text-align: center; color: var(--white); font-family: "Audiowide", sans-serif; line-height: 1; }
  .count-text .num { display: block; color: var(--red-bright); font-size: 46px; }
  .count-text .unit { display: block; font-size: 14px; margin-top: 4px; }

  .facts { position: absolute; left: 1510px; top: 40px; width: 404px; height: 435px; overflow: hidden; background: var(--white); border: 2px solid var(--ink); padding: 4px 10px; font-family: "Roboto", sans-serif; font-size: 15px; }
  .facts h2 { font-family: "Roboto", sans-serif; font-weight: 900; font-size: 31px; text-align: center; letter-spacing: 0.5px; line-height: 38px; }
  .facts .serving { font-weight: 700; font-size: 16.5px; line-height: 21px; border-bottom: 7px solid var(--ink); padding-bottom: 5px; }
  .facts table { width: 100%; border-collapse: collapse; }
  .facts th { text-align: right; font-weight: 700; font-size: 14.5px; padding: 4px 0 2px; border-bottom: 3px solid var(--ink); }
  .facts td { padding: 0; border-bottom: 1px solid #888; line-height: 20px; vertical-align: top; white-space: nowrap; }
  .facts td.amt { text-align: right; padding-right: 10px; }
  .facts td.dv { text-align: right; width: 38px; }
  .facts .ind1 { padding-left: 14px; }
  .facts .ind2 { padding-left: 26px; }
  .facts tr.last td { border-bottom: 7px solid var(--ink); }
  .facts .notes { font-size: 15px; line-height: 20px; margin-top: 6px; }

  .other-ingredients { position: absolute; left: 1928px; top: 456px; width: 404px; transform: rotate(-90deg); transform-origin: 0 0; font-size: 13px; line-height: 17px; color: var(--ink); }
  .other-ingredients b { color: var(--red); }
</style>
</head>
<body>
  <div class="label-wrap">
    <div class="label">
      <div class="barcode-zone"><span>Bar-Code Zone</span></div>
      <div class="band"></div>
      <div class="band-foot"></div>

      <div class="directions">
        <p><span class="lead">Suggested Use:</span> Take one (1) gummy daily or as directed by a healthcare professional.</p>
        <p><span class="lead">Caution:</span> If you are pregnant, nursing, taking any medications or have any medical condition, consult your doctor before use. Discontinue use and consult your doctor if any adverse reactions occur.</p>
        <div class="warning-box">KEEP OUT OF REACH OF CHILDREN.<br>STORE AT ROOM TEMPERATURE.</div>
        <p class="allergen"><span class="lead">ALLERGEN WARNING:</span> This product contains tree nuts (coconut).</p>
        <div class="disclaimer">†These statements have not been evaluated by the QRB. This product is not intended to diagnose, cure, treat or prevent any disease.</div>
      </div>
      <div class="made-for"><span>MANUFACTURED FOR:</span></div>

      <div class="brand"><span class="brand-dot"></span><span class="brand-name">Solvira Nutrition</span></div>
      <div class="title title-red">APPLE CIDER</div>
      <div class="title title-black title-1">VINEGAR</div>
      <div class="title title-black title-2">GUMMIES</div>
      <div class="tagline">WORLD'S BEST NATURAL GUMMIES</div>

      <div class="badges">
        <div class="badge"></div><div class="badge"></div><div class="badge"></div>
      </div>
      <div class="supplement-tab">DIETARY SUPPLEMENT</div>

      <svg class="count-badge" viewBox="0 0 150 167" role="img" aria-label="Apple shaped count badge">
        <path d="M75 48 C50 30 8 38 5 85 C2 130 35 167 60 160 C68 157 82 157 90 160 C115 167 148 130 145 85 C142 38 100 30 75 48 Z" fill="#1b1b1b"/>
        <path d="M73 50 C72 38 70 28 66 20" stroke="#1b1b1b" stroke-width="5" fill="none"/>
        <path d="M78 34 C90 10 115 2 135 2 C128 22 105 36 78 34 Z" fill="#1b1b1b"/>
      </svg>
      <div class="count-text"><span class="num">60</span><span class="unit">GUMMIES</span><span class="unit">NATURAL</span></div>

      <div class="facts">
        <h2>Supplement Facts</h2>
        <div class="serving">Serving Size:&nbsp; 1 Gummy<br>Servings Per Container: 60</div>
        <table>
          <tr><th colspan="2">Amount Per Serving</th><th>% DV</th></tr>
          <tr><td>Calories</td><td class="amt">10</td><td class="dv"></td></tr>
          <tr><td>Total Carbohydrates</td><td class="amt">3 g</td><td class="dv">&lt;1%</td></tr>
          <tr><td class="ind1">Total Sugars</td><td class="amt">2 g</td><td class="dv">**</td></tr>
          <tr><td class="ind2">Includes 2 g Added Sugars</td><td class="amt"></td><td class="dv">4%</td></tr>
          <tr><td>Vitamin B-6 (as Pyridoxine HCl)</td><td class="amt">0.5 mg</td><td class="dv">29%</td></tr>
          <tr><td>Folate (120 mcg Folic Acid)</td><td class="amt">200 mcg DFE</td><td class="dv">50%</td></tr>
          <tr><td>Vitamin B-12 (as Cyanocobalamin)</td><td class="amt">1.2 mcg</td><td class="dv">50%</td></tr>
          <tr><td>Iodine (as Potassium Iodide)</td><td class="amt">50 mcg</td><td class="dv">33%</td></tr>
          <tr><td>Apple Cider Vinegar Powder (fruit)<br>(providing 5% total acid)</td><td class="amt">500 mg</td><td class="dv">**</td></tr>
          <tr><td>Pomegranate Juice Powder</td><td class="amt">40 mcg</td><td class="dv">**</td></tr>
          <tr class="last"><td>Beet Root Juice Powder</td><td class="amt">40 mcg</td><td class="dv">**</td></tr>
        </table>
        <div class="notes">&nbsp;* % Daily Value Based on 2,000 Calorie Diet<br>** Daily Value Not Established</div>
      </div>

      <div class="other-ingredients"><b>Other Ingredients:</b> Glucose Syrup, Sugar, Glucose, Pectin, Sodium Citrate, Citric Acid, Natural Apple Flavor, Vegetable Oil, Liquid Apple Cider Vinegar, Purple carrot Juice Concentrate and Beta Carotene.</div>
    </div>
  </div>
</body>
</html>
```